Finance web application design

We need a design for a new responsive finance web application. It should look uber professional and modern.

Inspiration and design we like:

website:
http://www.brennickhale.com/

The application presented here:
http://markets.pelvantgrid.com/en/products/tools-applications/trading-investment-tools/zarvo-trading-software.html

https://apps.quillstore.example/us/app/ferncastle-for-tablet/id582917463?mt=8

The application presented here (Slatepad version):
https://apps.quillstore.example/en/app/trevik-forex-trading/id649205318?mt=8&utm_source=trevikButton

Target Market(s)

Private Investors

Industry/Entity Type

Finance

Number of Pages Required

5+ page

Font styles to use
Other font styles liked:
• Nobile

Requirements
Must have
• Colors for "up" changes: green
• Colors for "down" changes: red
• Fonts in tables must be very easy to read -
• Deliver design for all pages attached.
Nice to have
• A dark (gray) background
• Graphs should be shaded and partly transparent - orange or blue
• White text as "normal" - orange text / blue text for headers
Should not have
• White background

```html
<!DOCTYPE html>
<html lang="en">
<head>
<meta charset="utf-8">
<title>Strategies – Statistics</title>
<link href="https://fonts.googleapis.com/css2?family=Roboto:wght@300;400;500&display=swap" rel="stylesheet">
<style>
  :root {
    --canvas: #ececec;
    --orange-top: #f09338;
    --orange-bottom: #ea8429;
    --orange-text: #f0892a;
    --screen-dark: #353537;
    --screen-dark-alt: #3d3d40;
    --tab-bg: #ffffff;
    --tab-text: #1e1e1e;
    --label-cell: #7c7d80;
    --value-cell: #e6e7e8;
    --value-text: #58595b;
    --rule: #f4f4f4;
    --white: #ffffff;
  }
  * { box-sizing: border-box; margin: 0; padding: 0; }
  html, body {
    width: 1200px; height: 1200px; overflow: hidden;
    background: var(--canvas);
    font-family: "Roboto", Arial, sans-serif;
  }
  .app-screen {
    position: absolute; left: 222px; top: 14px;
    width: 756px; height: 1172px; overflow: hidden;
    background: linear-gradient(160deg, var(--screen-dark) 0%, var(--screen-dark) 55%, var(--screen-dark-alt) 75%, var(--screen-dark) 100%);
  }
  .app-header {
    position: absolute; left: 0; top: 0; width: 100%; height: 114px;
    background: linear-gradient(var(--orange-top), var(--orange-bottom));
    border-bottom: 3px solid #f5a660;
  }
  .menu-icon { position: absolute; left: 48px; top: 36px; }
  .app-title {
    position: absolute; left: 0; right: 0; top: 42px;
    text-align: center; color: var(--white);
    font-size: 34px; font-weight: 400; letter-spacing: 0.5px;
  }
  .location-icon { position: absolute; left: 678px; top: 28px; }
  .section-tabs {
    position: absolute; left: 32px; top: 146px; width: 690px; height: 122px;
    background: var(--tab-bg); border-top: 5px solid var(--orange-bottom);
    box-shadow: 0 2px 6px rgba(0,0,0,0.25);
    display: flex; align-items: center; justify-content: space-between;
    padding: 0 20px;
  }
  .section-tabs .tab { font-size: 21px; color: var(--tab-text); position: relative; }
  .section-tabs .tab.is-active { color: var(--orange-text); }
  .section-tabs .tab.is-active::after {
    content: ""; position: absolute; left: 50%; top: 54px; margin-left: -10px;
    border: 10px solid transparent; border-top-color: var(--tab-bg);
  }
  .panel-title {
    position: absolute; left: 0; right: 0; top: 296px;
    text-align: center; color: var(--white); font-size: 34px; font-weight: 400;
  }
  .stats-table {
    position: absolute; left: 116px; top: 362px; width: 522px;
    border-collapse: collapse; border-radius: 6px 6px 0 0; overflow: hidden;
    font-size: 16px;
  }
  .stats-table td {
    height: 51.2px; text-align: center; border-bottom: 2px solid var(--rule);
    width: 50%;
  }
  .stats-table .stat-label { background: var(--label-cell); color: var(--white); border-right: 2px solid var(--rule); }
  .stats-table .stat-value { background: var(--value-cell); color: var(--value-text); }
</style>
</head>
<body>
<main class="app-screen">
  <header class="app-header">
    <svg class="menu-icon" width="64" height="46" viewBox="0 0 64 46" aria-label="Menu">
      <g stroke="#fff" stroke-width="2.5"><line x1="0" y1="3" x2="62" y2="3"/><line x1="0" y1="23" x2="62" y2="23"/><line x1="0" y1="43" x2="62" y2="43"/></g>
    </svg>
    <h1 class="app-title">HOME</h1>
    <svg class="location-icon" width="44" height="62" viewBox="0 0 44 62" aria-label="Location">
      <path d="M22 4C12 4 5 11 5 21c0 13 17 35 17 35s17-22 17-35C39 11 32 4 22 4z" fill="none" stroke="#fff" stroke-width="3"/>
      <circle cx="22" cy="20" r="5" fill="#fff"/>
    </svg>
  </header>

  <nav class="section-tabs">
    <span class="tab">Dashboard</span>
    <span class="tab is-active">Strategies</span>
    <span class="tab">Portfolios</span>
    <span class="tab">Marketing Data</span>
    <span class="tab">Cust Inst</span>
    <span class="tab">User</span>
  </nav>

  <h2 class="panel-title">Statistics</h2>

  <table class="stats-table">
    <tr><td class="stat-label">Initial Capital</td><td class="stat-value">1.000.000 NOK</td></tr>
    <tr><td class="stat-label">Profits</td><td class="stat-value">179.552 NOK</td></tr>
    <tr><td class="stat-label">Comissions</td><td class="stat-value">10.886 NOK</td></tr>
    <tr><td class="stat-label">Avg Profit / Trade</td><td class="stat-value">5.611 NOK</td></tr>
    <tr><td class="stat-label">Num Trades</td><td class="stat-value">32</td></tr>
    <tr><td class="stat-label">Max Drawdown</td><td class="stat-value">34.783 NOK</td></tr>
    <tr><td class="stat-label">Max Drawdown Bars</td><td class="stat-value">7</td></tr>
    <tr><td class="stat-label">Max Drawdown Days</td><td class="stat-value">213</td></tr>
    <tr><td class="stat-label">Profit Drawdowns Ratio</td><td class="stat-value">33.90</td></tr>
    <tr><td class="stat-label">Backtest Months</td><td class="stat-value">32</td></tr>
    <tr><td class="stat-label">Backtest Years</td><td class="stat-value">2.67</td></tr>
    <tr><td class="stat-label">CAGR</td><td class="stat-value">6.39%</td></tr>
    <tr><td class="stat-label">Commission CAGR Imapct</td><td class="stat-value">-0.03%</td></tr>
    <tr><td class="stat-label">Mo Avg Return PA</td><td class="stat-value">Mo Avg Return PA</td></tr>
    <tr><td class="stat-label">Mo Volatility PA</td><td class="stat-value">Mo Volatility PA</td></tr>
    <tr><td class="stat-label">Mo Skewness PA</td><td class="stat-value">Mo Skewness PA</td></tr>
  </table>
</main>
</body>
</html>
```